Brochure Design*

We are seeking a simple but powerful brochure design for our new company that uses electrostatic sprayers for the treatment and prevention of Covid 19 for businesses throughout the Southeast. The current brochure has too many photos and very distracting, i personally do not like anything about the brochure. Our sister company Harlow Print Supply was founded in 1983. Our company HPS Services LLC website is www.hpsvx.com
Updates

We need a few more days to receive feedback from our employees. Thank You

Target Market(s)

Business owners

Font styles to use
Serif
Sans Serif

Requirements
Must have
• A call for action brochure, simple while delivering a strong message
Should not have
• CLUTTER,

```html
<!DOCTYPE html>
<html lang="en">
<head>
<meta charset="utf-8">
<title>HPS Services LLC</title>
<link rel="stylesheet" href="https://fonts.googleapis.com/css2?family=Share+Tech&display=swap">
<style>
  :root {
    --cream: #fbe4a9;
    --teal-deep: #2d5f6b;
    --teal-mid: #4f8690;
    --teal-pale: #8fb6ba;
  }
  html, body { margin: 0; padding: 0; overflow: hidden; }
  body { width: 927px; height: 1200px; background: var(--teal-mid); }
  .brochure-cover {
    position: relative;
    width: 927px;
    height: 1200px;
    overflow: hidden;
    background: var(--teal-mid);
  }
  .cover-backdrop { position: absolute; inset: 0; }
  .frame { position: absolute; inset: 0; }
  .company-name {
    position: absolute; left: 0; right: 0; top: 372px;
    margin: 0; text-align: center; color: var(--cream);
    font-family: "Share Tech", sans-serif;
    font-weight: 400;
    font-size: 70px; line-height: 1;
    letter-spacing: 1px;
  }
  .name-rule {
    position: absolute; left: 162px; top: 493px;
    width: 611px; height: 2px; background: var(--cream);
  }
  .tagline {
    position: absolute; left: 0; right: 0; top: 862px;
    margin: 0; text-align: center; color: var(--cream);
    font-family: "Share Tech", sans-serif;
    font-size: 27px; line-height: 36px;
    font-variant: small-caps; letter-spacing: 4px;
  }
  .website {
    position: absolute; left: 0; right: 0; top: 1083px;
    margin: 0; text-align: center; color: var(--cream);
    font-family: "Share Tech", sans-serif;
    font-size: 24px; letter-spacing: 5px;
  }
</style>
</head>
<body>
<main class="brochure-cover">
  <svg class="cover-backdrop" width="927" height="1200" viewBox="0 0 927 1200" role="img" aria-label="Photo of two workers in protective suits disinfecting a washroom sink area, tinted teal">
    <defs>
      <linearGradient id="photoTint" x1="0" y1="0" x2="1" y2="1">
        <stop offset="0" stop-color="#5f939b"/>
        <stop offset="0.5" stop-color="#4f8690"/>
        <stop offset="1" stop-color="#6a9da4"/>
      </linearGradient>
    </defs>
    <rect width="927" height="1200" fill="url(#photoTint)"/>
    <path d="M150 0 H927 V520 C880 600 760 735 600 735 C420 735 250 640 175 470 C140 390 140 200 150 0 Z" fill="var(--teal-deep)" opacity="0.85"/>
    <path d="M0 200 C120 260 200 330 240 470 C300 700 260 980 240 1200 H0 Z" fill="var(--teal-pale)" opacity="0.55"/>
    <path d="M927 520 C860 640 840 820 880 1200 H927 Z" fill="var(--teal-pale)" opacity="0.45"/>
  </svg>

  <svg class="frame" width="927" height="1200" viewBox="0 0 927 1200" aria-hidden="true">
    <g fill="none" stroke="var(--cream)" stroke-width="5">
      <line x1="12" y1="30" x2="915" y2="30"/>
      <line x1="12" y1="1167" x2="915" y2="1167"/>
      <line x1="33" y1="12" x2="33" y2="1188"/>
      <line x1="894" y1="12" x2="894" y2="1188"/>
    </g>
    <g fill="var(--cream)">
      <rect x="18" y="18" width="18" height="18"/>
      <rect x="891" y="18" width="18" height="18"/>
      <rect x="18" y="1161" width="18" height="18"/>
      <rect x="891" y="1161" width="18" height="18"/>
      <rect x="8" y="702" width="24" height="20"/>
      <rect x="895" y="702" width="24" height="20"/>
    </g>
  </svg>

  <h1 class="company-name">HPS Services LLC</h1>
  <div class="name-rule"></div>

  <p class="tagline">Preventing Infection Transmission<br>Keeping you and your clients infection-free</p>
  <p class="website">hpsservicesvx.com</p>
</main>
</body>
</html>
```